Business card design needed

Bright Path Ahead is an online wellness program designed for people dealing with cancer to take control of their lives and Bright path ahead.

Target Market(s)

initially woman aged 35 to 65 years eventaully then men

Industry/Entity Type

Business

Contact Information for Business Card

Marisol Dunkerly
Bright path ahead Coach
Marisol@brightpathahead.com.au
M 0419382716
Skype Marisol.Dunkerly
local number to come
www.brightpathahead.com.au

Requirements
Must have
• Business cards want to have a photo of me on the back this is a head shot. Also a small blurb " Marisol recovered and survived 2 types of cancer. She under went a transformational 12 month journey to overcome cancer naturally . Join her online coaching program to Bright path ahead.

Phone number and email and skype address.
Nice to have
• Looking for something that resembles health EG abstract tree of life, or something resembling health and balance . Like lime green/apple green want modern fresh. Want only 2 colours used on the cards. Need to use the logo and Bright path ahead on website and email signature - Clean and fresh

Also would like Letter head and logo for website and email signature

```html
<!DOCTYPE html>
<html lang="en">
<head>
<meta charset="utf-8">
<title>Bright Path Ahead – Business Card</title>
<link href="https://fonts.googleapis.com/css2?family=Quicksand:wght@500;700&family=Didact+Gothic&display=swap" rel="stylesheet">
<style>
  :root {
    --teal: #1a9dbb;
    --link-blue: #1a84c4;
    --bark: #5b4a40;
    --body-grey: #5a5a5a;
    --card-bg: #f2f2ee;
    --page-bg: #ffffff;
  }
  * { margin: 0; padding: 0; box-sizing: border-box; }
  html, body { width: 1200px; height: 355px; overflow: hidden; background: var(--page-bg); }
  .canvas { position: relative; width: 1200px; height: 355px; }

  .card { position: absolute; background: var(--card-bg); overflow: hidden; }
  .card--back { left: 30px; top: 33px; width: 487px; height: 275px; }
  .card--front { left: 688px; top: 33px; width: 485px; height: 280px; }

  /* Back side */
  .portrait {
    position: absolute; z-index: 0; left: 250px; top: 0; width: 237px; height: 275px;
    background: radial-gradient(ellipse at 50% 45%, #e9ddd0 0%, #f4efe9 45%, #f7f6f3 75%),
                linear-gradient(180deg, #f7f6f3, #eeeae5);
  }
  .brand-mark {
    position: absolute; z-index: 1; left: 78px; top: 120px;
    display: flex; align-items: center; gap: 6px;
    font-family: "Quicksand", sans-serif; font-weight: 700;
    font-size: 14px; color: var(--teal);
  }
  .brand-mark__dot { width: 12px; height: 12px; border-radius: 50%; background: var(--teal); }
  .blurb {
    position: absolute; z-index: 1; left: 29px; top: 150px; width: 226px;
    font-family: "Didact Gothic", sans-serif; font-size: 12.5px; line-height: 13px;
    color: var(--body-grey);
  }
  .blurb p { margin-bottom: 4px; }
  .blurb__web {
    position: absolute; z-index: 1; left: 29px; top: 241px;
    font-family: "Quicksand", sans-serif; font-weight: 700; font-size: 12px;
    color: var(--link-blue);
  }

  /* Front side */
  .emblem {
    position: absolute; left: 40px; top: 60px; width: 150px; height: 150px;
    border-radius: 50%; background: var(--teal); opacity: 0.9;
  }
  .identity { position: absolute; left: 209px; top: 50px; }
  .identity__name {
    font-family: "Quicksand", sans-serif; font-weight: 700;
    font-size: 29px; letter-spacing: 1px; color: var(--teal); line-height: 1;
  }
  .identity__role {
    margin-top: 6px;
    font-family: "Quicksand", sans-serif; font-weight: 700;
    font-size: 15px; color: var(--bark);
  }
  .contacts { position: absolute; left: 210px; top: 117px; list-style: none; }
  .contacts li {
    display: flex; align-items: center; gap: 6px; height: 24.5px;
    font-family: "Quicksand", sans-serif; font-weight: 700; font-size: 13px;
    color: var(--bark);
  }
  .contacts svg { width: 18px; height: 18px; flex: none; }
  .web-bar {
    position: absolute; left: 210px; top: 230px; width: 275px; height: 20px;
    background: var(--teal); padding-left: 8px;
    font-family: "Quicksand", sans-serif; font-weight: 700; font-size: 14.5px;
    letter-spacing: 0.8px; color: #fff; line-height: 20px;
  }
</style>
</head>
<body>
<div class="canvas">

  <section class="card card--back">
    <div class="portrait" role="img" aria-label="Portrait photo of the coach in white with a turquoise necklace"></div>
    <div class="brand-mark"><span class="brand-mark__dot"></span>Bright Path Ahead</div>
    <div class="blurb">
      <p>Marisol recovered and survived two types of cancer.</p>
      <p>She took a transformational journey to overcome cancer naturally.</p>
      <p>Join her online coaching program to bright path ahead.</p>
    </div>
    <div class="blurb__web">www.brightpathahead.com.au</div>
  </section>

  <section class="card card--front">
    <div class="emblem"></div>
    <div class="identity">
      <h1 class="identity__name">Marisol Dunkerly</h1>
      <p class="identity__role">Bright Path Ahead Coach</p>
    </div>
    <ul class="contacts">
      <li>
        <svg viewBox="0 0 18 18"><rect width="18" height="18" rx="4" fill="var(--teal)"/><rect x="6" y="3" width="6" height="12" rx="1.2" fill="none" stroke="#fff" stroke-width="1.4"/><circle cx="9" cy="13" r="0.8" fill="#fff"/></svg>
        M 0419382716
      </li>
      <li>
        <svg viewBox="0 0 18 18"><circle cx="9" cy="9" r="9" fill="var(--teal)"/><rect x="4" y="5.5" width="10" height="7" fill="#fff"/><path d="M4 5.5 L9 9.5 L14 5.5" fill="none" stroke="var(--teal)" stroke-width="1"/></svg>
        Marisol@brightpathahead.com.au
      </li>
      <li>
        <svg viewBox="0 0 18 18"><circle cx="9" cy="9" r="9" fill="var(--teal)"/></svg>
        Marisol.Dunkerly
      </li>
      <li>
        <svg viewBox="0 0 18 18"><circle cx="9" cy="9" r="9" fill="var(--teal)"/><path d="M6 4.5 L7.8 4.5 L8.5 7 L7.3 8 Q8.3 10 10 10.8 L11 9.6 L13.5 10.3 L13.5 12 Q13 13.5 11.5 13.5 Q5 12.5 4.5 6 Q4.5 4.8 6 4.5 Z" fill="#fff"/></svg>
        +61390257718
      </li>
    </ul>
    <div class="web-bar">www.brightpathahead.com.au</div>
  </section>

</div>
</body>
</html>
```